New Business Tri Fold Brochure

Tri Fold Brochure for new business. I have attached a few versions of our logo and would like the color scheme to be the blue and grey colors from the logo. I have also attached examples of the data that I would like implemented into the brochure such as the FAQ's and general company information. I would like the 3 general points (hassle free, save money, no risk guarantee) to be matched to appropriate icons. I also need the 3 steps for "how it works" matched to appropriate themed icons. I would like the back of the brochure to have a photo of our building, map of location and all contact information. Address: 728 W. Brindle Crest Ave Suite 410 Fort Lauderdale FL 33417. Phone- 754-618-2094. Email: info@harbor-tallyworks.com. Website: www.harbor-tallyworks.com

```html
<!DOCTYPE html>
<html lang="en">
<head>
<meta charset="utf-8">
<title>Harbor Tallyworks Tri-Fold Brochure</title>
<link href="https://fonts.googleapis.com/css2?family=Montserrat:wght@600;700;800&family=Roboto:wght@500;700&family=Open+Sans:wght@400;600&display=swap" rel="stylesheet">
<style>
:root{
  --blue:#1f6fc0;
  --blue-deep:#1a60aa;
  --grey:#8c9198;
  --ink:#222629;
  --paper:#ffffff;
  --canvas:#ececec;
  --hair:#d7dde4;
}
*{box-sizing:border-box;margin:0;padding:0}
html,body{width:669px;height:1200px;overflow:hidden}
body{background:var(--canvas);font-family:"Open Sans",Arial,sans-serif;color:var(--ink);position:relative}
.spread{position:absolute;left:20px;width:629px;height:444px;display:grid;grid-template-columns:210px 209px 210px;background:var(--paper);box-shadow:0 2px 8px rgba(0,0,0,.18)}
.spread-outside{top:146px}
.spread-inside{top:610px}
.panel{position:relative;overflow:hidden;display:flex;flex-direction:column}
.photo{flex:none}
h2,h3{font-family:"Roboto",Arial,sans-serif}
/* FAQ */
.faq{background:var(--blue);color:#fff;padding:14px 14px 0 19px;height:302px}
.faq h2{font-size:17px;font-weight:700;margin-bottom:2px}
.faq h3{font-size:7.4px;font-weight:500;margin-top:8px;line-height:1.25}
.faq p{font-size:4.7px;line-height:1.45;margin-top:2px}
.photo-savings{height:142px;background:linear-gradient(120deg,#cfcfcf,#bdbdbd 60%,#a9a9a9)}
/* contact */
.photo-building{height:146px;background:linear-gradient(180deg,#dfe6ee,#8f9ea8 45%,#4d5a4a 80%,#6d6d6a)}
.contact{flex:1;padding:18px 13px 0}
.brand{font-family:"Montserrat",Arial,sans-serif;font-weight:700;display:flex;align-items:center;gap:5px}
.brand .dot{width:11px;height:11px;border-radius:50%;background:currentColor;flex:none}
.contact .brand{color:var(--blue);font-size:10px}
.contact h2{color:var(--blue);font-size:11px;font-weight:500;margin:12px 0 10px}
.contact ul{list-style:none}
.contact li{display:flex;gap:6px;align-items:flex-start;font-size:5.7px;font-weight:600;margin-bottom:8px;line-height:1.3}
.contact svg{width:8px;height:8px;flex:none;fill:var(--blue)}
.map{height:140px;background:linear-gradient(135deg,#eef0f1,#f4e7c2 45%,#e9ecef 70%,#b9d3ef);border-top:1px solid var(--hair)}
/* cover */
.cover{background:var(--blue);color:#fff;align-items:center}
.cover-art{position:absolute;top:0;left:0;width:210px;height:250px}
.cover-body{margin-top:270px;text-align:center}
.cover .brand{font-size:12px;justify-content:center}
.headline{font-family:"Montserrat",Arial,sans-serif;font-weight:800;font-size:20px;line-height:1.02;margin-top:22px}
.tagline{font-family:"Montserrat",Arial,sans-serif;font-weight:700;font-size:11px;margin-top:4px}
.cover .url{font-family:"Montserrat",Arial,sans-serif;font-weight:600;font-size:6px;letter-spacing:.08em;margin-top:26px}
/* benefits */
.benefits{padding:14px 10px 0;text-align:center;height:238px}
.benefit{margin-bottom:12px}
.icon{width:19px;height:19px;border-radius:50%;border:1.4px solid var(--blue);display:inline-flex;align-items:center;justify-content:center}
.icon svg{width:11px;height:11px}
.benefit h3{color:var(--blue);font-size:8.6px;font-weight:500;margin-top:1px}
.benefit p{font-size:5.6px;line-height:1.35}
.photo-team{flex:1;background:linear-gradient(160deg,#f2f4f6,#d9dde2 45%,#2f4a75 80%,#243a5e)}
/* who/what */
.blue-block{background:var(--blue);color:#fff;padding:12px 13px}
.blue-block h2{font-size:8.6px;font-weight:500;margin-bottom:9px}
.blue-block p{font-size:5.9px;line-height:1.38}
.who{height:119px}
.photo-city{height:182px;background:linear-gradient(180deg,#e8eef6,#c6d4e6 45%,#5f7fa6 80%,#3c5f89)}
.what{flex:1;padding-top:16px}
/* steps */
.photo-desk{height:178px;background:linear-gradient(160deg,#f3f3f2,#cfd2d4 50%,#6a6e70)}
.steps{flex:1;border-top:2px solid var(--blue);padding:10px 14px 0;background:linear-gradient(180deg,#fff,#f1f6fb)}
.steps h2{color:var(--blue);font-size:9.6px;font-weight:500;margin-bottom:8px}
.step{margin-bottom:8px}
.step-head{display:flex;align-items:center;gap:5px;color:var(--blue);font-family:"Roboto",Arial,sans-serif;font-weight:500;font-size:7.4px;line-height:1.1}
.step-head .icon{width:18px;height:18px;background:var(--blue);border:2px solid #cfe0f2;flex:none}
.step p{font-size:5.4px;line-height:1.35;margin-top:4px}
</style>
</head>
<body>

<section class="spread spread-outside" aria-label="Brochure outside">
  <div class="panel">
    <div class="faq">
      <h2>FAQ</h2>
      <h3>How does it work?</h3>
      <p>It's easy! Enroll in the service and either include a copy of your bill or provide your login credentials. We do the rest! Our team of experts will battle with your provider to save you money. Within 2-3 business days, you will receive an email and phone call from our experts explaining the results of our negotiations.</p>
      <h3>How will I receive my savings?</h3>
      <p>Your provider will apply the promised reductions to your bill in the next billing cycle. In some cases, we can even get your provider to make your new lower rates retroactive back to the first of the current month!</p>
      <h3>Will you switch my service provider without asking?</h3>
      <p>No. We will never switch your service provider. Our goal is to save you as much money as possible, while keeping you with your current provider.</p>
      <h3>How much does Harbor Tallyworks cost?</h3>
      <p>Our fee is 50% of your savings for the first 12 months, earned only when we do our job effectively! If we are unable to save you any money, there is no charge for our service. After the initial negotiation, we will continually monitor your rates on a monthly basis to ensure you are getting the absolute best rates.</p>
      <h3>Are there any risks involved?</h3>
      <p>No. There are no risks and there are also no fees if we cannot save you money.</p>
    </div>
    <div class="photo photo-savings" role="img" aria-label="Open hand holding a rising bar chart"></div>
  </div>

  <div class="panel">
    <div class="photo photo-building" role="img" aria-label="Office building exterior with palm trees"></div>
    <div class="contact">
      <div class="brand"><span class="dot"></span>Harbor Tallyworks</div>
      <h2>Contact us</h2>
      <ul>
        <li><svg viewBox="0 0 24 24"><path d="M6.6 10.8a15 15 0 0 0 6.6 6.6l2.2-2.2c.3-.3.7-.4 1-.2 1.1.4 2.3.6 3.6.6.6 0 1 .4 1 1V20c0 .6-.4 1-1 1A17 17 0 0 1 3 4c0-.6.4-1 1-1h3.5c.6 0 1 .4 1 1 0 1.3.2 2.5.6 3.6.1.3 0 .7-.2 1z"/></svg>754-618-2094</li>
        <li><svg viewBox="0 0 24 24"><path d="M2 5h20v14H2zm2 2v.5l8 5 8-5V7z"/></svg>info@harbor-tallyworks.com</li>
        <li><svg viewBox="0 0 24 24"><path d="M12 2a10 10 0 1 0 0 20 10 10 0 0 0 0-20zm6.9 6h-3a15 15 0 0 0-1.3-3.9A8 8 0 0 1 18.9 8zM12 4c.8 1.2 1.5 2.5 1.9 4h-3.8c.4-1.5 1.1-2.8 1.9-4zM4.3 14a8 8 0 0 1 0-4h3.4a16 16 0 0 0 0 4zm.8 2h3a15 15 0 0 0 1.3 3.9A8 8 0 0 1 5.1 16zm3-8h-3a8 8 0 0 1 4.3-3.9C8.8 5.3 8.4 6.6 8.1 8zM12 20c-.8-1.2-1.5-2.5-1.9-4h3.8c-.4 1.5-1.1 2.8-1.9 4zm2.3-6H9.7a14 14 0 0 1 0-4h4.6a14 14 0 0 1 0 4zm.3 5.9c.6-1.2 1-2.5 1.3-3.9h3a8 8 0 0 1-4.3 3.9zm1.7-5.9a16 16 0 0 0 0-4h3.4a8 8 0 0 1 0 4z"/></svg>www.harbor-tallyworks.com</li>
        <li><svg viewBox="0 0 24 24"><path d="M12 2a7 7 0 0 0-7 7c0 5 7 13 7 13s7-8 7-13a7 7 0 0 0-7-7zm0 9.5a2.5 2.5 0 1 1 0-5 2.5 2.5 0 0 1 0 5z"/></svg>728 W. Brindle Crest Ave Suite 410 Fort Lauderdale<br>FL 33417</li>
      </ul>
    </div>
    <div class="photo map" role="img" aria-label="Street map of the office location"></div>
  </div>

  <div class="panel cover">
    <svg class="cover-art" viewBox="0 0 210 250" aria-hidden="true">
      <path d="M14 0H210V236Q150 262 88 236Q10 196 14 0Z" fill="none" stroke="#fff" stroke-width="4"/>
      <path d="M19 0H210V230Q150 255 90 229Q16 192 19 0Z" fill="url(#coverPhoto)" role="img" aria-label="Business handshake over a city skyline at dusk"/>
      <defs><linearGradient id="coverPhoto" x1="0" y1="0" x2="0" y2="1"><stop offset="0" stop-color="#e7cfc9"/><stop offset=".45" stop-color="#6b5f63"/><stop offset="1" stop-color="#2a2a33"/></linearGradient></defs>
    </svg>
    <div class="cover-body">
      <div class="brand"><span class="dot"></span>Harbor Tallyworks</div>
      <div class="headline">HASSLE FREE<br>SAVE MONEY</div>
      <div class="tagline">NO RISK GUARANTEE</div>
      <div class="url">www.harbor-tallyworks.com</div>
    </div>
  </div>
</section>

<section class="spread spread-inside" aria-label="Brochure inside">
  <div class="panel">
    <div class="benefits">
      <div class="benefit">
        <span class="icon"><svg viewBox="0 0 24 24"><path d="M4 12l5 5L20 6" fill="none" stroke="#1f6fc0" stroke-width="3.4" stroke-linecap="round" stroke-linejoin="round"/></svg></span>
        <h3>Hassle Free</h3>
        <p>You're busy running a business; let us negotiate<br>for you and put money back in your pocket!</p>
      </div>
      <div class="benefit">
        <span class="icon"><svg viewBox="0 0 24 24"><circle cx="12" cy="12" r="10" fill="#1f6fc0"/><text x="12" y="16.5" text-anchor="middle" font-size="13" font-family="Arial" font-weight="700" fill="#fff">$</text></svg></span>
        <h3>Save Money</h3>
        <p>We save business owners an average of<br>$500 per month</p>
      </div>
      <div class="benefit">
        <span class="icon"><svg viewBox="0 0 24 24"><path d="M12 2l8 3v6c0 5-3.5 9-8 11-4.5-2-8-6-8-11V5z" fill="#1f6fc0"/><path d="M8 12l3 3 5-6" fill="none" stroke="#fff" stroke-width="2"/></svg></span>
        <h3>No Risk Guarantee</h3>
        <p>We guarantee we will lower your bill or there is no<br>charge for our service!</p>
      </div>
    </div>
    <div class="photo photo-team" role="img" aria-label="Two colleagues reviewing documents in an office"></div>
  </div>

  <div class="panel">
    <div class="blue-block who">
      <h2>WHO WE ARE</h2>
      <p>Harbor Tallyworks is a company that was founded by previous merchant processing professionals with over 20 years of industry knowledge and experience. We know all of the tricks that the big companies use to fill their pockets with your money! We use that industry</p>
    </div>
    <div class="photo photo-city" role="img" aria-label="Silhouettes of business people blended with a city skyline"></div>
    <div class="blue-block what">
      <h2>WHAT WE DO</h2>
      <p>Once you sign up, our experts get to work negotiating with your current merchant processing provider. Our goal is to get you the lowest rates possible without changing providers or having to get expensive new equipment. We offer a No Risk Savings Guarantee. If we can't save you money, you don't pay us a dime! 100% risk free.</p>
    </div>
  </div>

  <div class="panel">
    <div class="photo photo-desk" role="img" aria-label="Person working on a laptop at a desk with coffee"></div>
    <div class="steps">
      <h2>HOW IT WORKS</h2>
      <div class="step">
        <div class="step-head"><span class="icon"><svg viewBox="0 0 24 24"><circle cx="12" cy="8" r="4" fill="#fff"/><path d="M4 21c0-4.4 3.6-7 8-7s8 2.6 8 7z" fill="#fff"/></svg></span>Sign Up</div>
        <p>Provide some basic information and a copy of<br>your most recent</p>
      </div>
      <div class="step">
        <div class="step-head"><span class="icon"><svg viewBox="0 0 24 24"><path d="M6.6 10.8a15 15 0 0 0 6.6 6.6l2.2-2.2c.3-.3.7-.4 1-.2 1.1.4 2.3.6 3.6.6.6 0 1 .4 1 1V20c0 .6-.4 1-1 1A17 17 0 0 1 3 4c0-.6.4-1 1-1h3.5c.6 0 1 .4 1 1 0 1.3.2 2.5.6 3.6.1.3 0 .7-.2 1z" fill="#fff"/></svg></span>We Contact Your<br>Provider</div>
        <p>Our experts get to work negotiating with your current provider on your behalf for the lowest rates possible</p>
      </div>
      <div class="step">
        <div class="step-head"><span class="icon"><svg viewBox="0 0 24 24"><text x="12" y="18" text-anchor="middle" font-size="17" font-family="Arial" font-weight="700" fill="#fff">$</text></svg></span>You Save Money</div>
        <p>Your monthly fee's get reduced and you save money! We split the savings for the first year and the</p>
      </div>
    </div>
  </div>
</section>

</body>
</html>
```